Business Card Design

We sell fish products to corporate food companies who then turn these products into final food products for consumers

Industry/Entity Type

Business

Contact Information for Business Card

I need a corporate business card template for a fish products business. We would like it be professional for use in dealing with multi national companies. This company business card template will be used by multiple employees so the following fields must be open to edit (Name, Phone Number and Email address)

```html
<!DOCTYPE html>
<html lang="en">
<head>
<meta charset="utf-8">
<title>Tidemark Seafoods – Business Card</title>
<link rel="stylesheet" href="https://fonts.googleapis.com/css2?family=Source+Sans+3:wght@400;600&display=swap">
<style>
  :root {
    --backdrop: #5e534b;
    --card-white: #f7f6f2;
    --ocean-blue: #0f5aa6;
    --wave-teal: #1fb3c9;
    --brand-blue: #17539b;
    --icon-green: #5cbf7a;
    --text-white: #ffffff;
    --text-soft: #c9d9ee;
  }
  * { margin: 0; padding: 0; box-sizing: border-box; }
  html, body { width: 1200px; height: 800px; overflow: hidden; }
  body {
    background: var(--backdrop);
    font-family: "Source Sans 3", sans-serif;
    position: relative;
  }
  .business-card {
    position: absolute;
    left: 162px; top: 150px;
    width: 875px; height: 500px;
    background: var(--card-white);
    box-shadow: 0 12px 30px rgba(0,0,0,0.35);
    overflow: hidden;
  }
  .card-band { position: absolute; inset: 0; width: 875px; height: 500px; }
  .brand {
    position: absolute;
    left: 0; right: 0; top: 110px;
    display: flex; flex-direction: column; align-items: center;
    color: var(--brand-blue);
    font-weight: 600;
    line-height: 1;
  }
  .brand-mark {
    width: 58px; height: 58px; border-radius: 50%;
    background: var(--brand-blue);
    margin-bottom: 14px;
  }
  .brand-name { font-size: 46px; letter-spacing: 1px; }
  .brand-sub { font-size: 24px; letter-spacing: 7px; margin-top: 6px; }
  .person {
    position: absolute; left: 330px; top: 352px;
    color: var(--text-white);
    line-height: 1.1;
  }
  .person-name { font-size: 28px; font-weight: 400; }
  .person-title { font-size: 18px; color: var(--text-soft); margin-top: 2px; }
  .contact {
    position: absolute;
    display: flex; align-items: center; gap: 12px;
    color: var(--text-white); font-size: 25px;
    line-height: 1;
  }
  .contact-email { left: 470px; top: 412px; }
  .contact-phone { left: 50px; top: 454px; }
  .contact-icon {
    width: 32px; height: 32px; border-radius: 4px;
    background: var(--icon-green);
    display: flex; align-items: center; justify-content: center;
  }
</style>
</head>
<body>
  <div class="business-card">
    <svg class="card-band" viewBox="0 0 875 500" aria-hidden="true">
      <path d="M0 430 C 200 320, 480 250, 875 290 L875 500 L0 500 Z" fill="var(--wave-teal)"/>
      <path d="M0 442 C 200 332, 480 262, 875 300 L875 500 L0 500 Z" fill="var(--card-white)"/>
      <path d="M0 448 C 200 338, 480 268, 875 306 L875 500 L0 500 Z" fill="var(--ocean-blue)"/>
    </svg>

    <div class="brand">
      <div class="brand-mark"></div>
      <div class="brand-name">TIDEMARK</div>
      <div class="brand-sub">SEAFOODS</div>
    </div>

    <div class="person">
      <div class="person-name">Clara Ventrano</div>
      <div class="person-title">Managing Director</div>
    </div>

    <div class="contact contact-email">
      <span class="contact-icon">
        <svg width="20" height="14" viewBox="0 0 20 14" aria-hidden="true">
          <rect x="1" y="1" width="18" height="12" fill="none" stroke="#fff" stroke-width="1.6"/>
          <path d="M1 1 L10 8 L19 1" fill="none" stroke="#fff" stroke-width="1.6"/>
        </svg>
      </span>
      <span>clara.ventrano@example.com</span>
    </div>

    <div class="contact contact-phone">
      <span class="contact-icon">
        <svg width="18" height="18" viewBox="0 0 24 24" aria-hidden="true">
          <path d="M6.6 10.8a15.1 15.1 0 0 0 6.6 6.6l2.2-2.2c.3-.3.7-.4 1-.2 1.1.4 2.3.6 3.6.6.6 0 1 .4 1 1V20c0 .6-.4 1-1 1A17 17 0 0 1 3 4c0-.6.4-1 1-1h3.5c.6 0 1 .4 1 1 0 1.3.2 2.5.6 3.6.1.3 0 .7-.2 1z" fill="#fff"/>
        </svg>
      </span>
      <span>555-010-0147</span>
    </div>
  </div>
</body>
</html>
```